Financial Services Flyer for Healthcare Providers

We need a flyer design for a product of Talvo Financial (www.talvofinancial.example) called the PLUM program. Attached you will find the content for the flyer. Please use your own creativity and keep in mind the this is a product of Talvo Financial, a financial services company that works in the field of healthcare. If you have any questions or comments, please feel free to ask....

Target Market(s)

Our target audience is healthcare providers.

Industry/Entity Type

Financial

Requirements
Must have
• Eye catching graphics and colors but still look fairly conservative since our audience is somewhat conservative.
Nice to have
• Nice looking, smiling, upbeat people in pictorial portions of the flyer.
Should not have
• Our clients are all found in America, so the look, feel and subtext should all target an American audience and not have the look and feel of being from outside of the US.

```html
<!DOCTYPE html>
<html lang="en">
<head>
<meta charset="utf-8">
<title>PLUM Program Flyer – Talvo Financial</title>
<link href="https://fonts.googleapis.com/css2?family=Source+Sans+3:wght@400;600;700&display=swap" rel="stylesheet">
<style>
  :root {
    --page-bg: #e9e6e2;
    --paper: #ffffff;
    --ink: #2f2f2f;
    --charcoal: #333333;
    --band-gray: #555555;
    --orange: #f07022;
    --white: #ffffff;
    --photo-light: #dfe7ee;
    --photo-mid: #a9b7c6;
  }
  * { box-sizing: border-box; margin: 0; padding: 0; }
  html, body {
    width: 1000px; height: 1200px; overflow: hidden;
    background: var(--page-bg);
    font-family: "Source Sans 3", "Myriad Pro", Arial, sans-serif;
  }
  .flyer {
    position: absolute; left: 97px; top: 30px;
    width: 806px; height: 1140px;
    background: var(--paper);
    box-shadow: 0 6px 24px rgba(0,0,0,.18);
    overflow: hidden;
  }
  .hero {
    position: absolute; left: 0; top: 0; width: 806px; height: 452px;
    background:
      linear-gradient(90deg, rgba(47,61,85,.55) 0%, rgba(47,61,85,.25) 45%, rgba(255,255,255,0) 70%),
      linear-gradient(180deg, var(--photo-light) 0%, var(--photo-mid) 65%, #c9d2dc 100%);
  }
  .hero-title {
    position: absolute; left: 0; top: 174px; width: 806px; height: 136px;
    background: rgba(120,130,145,.45);
    text-align: center; color: var(--white);
  }
  .hero-title h1 { font-size: 48px; font-weight: 700; line-height: 1; margin-top: 26px; }
  .hero-title p { font-size: 21px; margin-top: 6px; }
  .hero-band {
    position: absolute; left: 0; top: 452px; width: 806px; height: 20px;
    background: var(--band-gray);
  }
  .intro {
    position: absolute; left: 0; top: 472px; width: 806px; height: 186px;
    background: linear-gradient(180deg, #e8e8e8 0%, #ffffff 18%);
    padding: 30px 32px 0 32px;
  }
  .intro h2 { font-size: 31px; font-weight: 700; color: var(--ink); line-height: 1.1; white-space: nowrap; }
  .accent { color: var(--orange); }
  .intro p { font-size: 18.5px; color: var(--ink); line-height: 1.2; margin-top: 8px; }
  .divider {
    position: absolute; left: 30px; top: 655px; width: 746px; height: 3px;
    background: linear-gradient(90deg, rgba(0,0,0,0), #888 20%, #888 80%, rgba(0,0,0,0));
  }
  .panel {
    position: absolute; top: 683px; height: 332px;
    background: var(--charcoal);
    box-shadow: 0 4px 8px rgba(0,0,0,.35);
    color: var(--white);
  }
  .how { left: 0; width: 615px; padding: 34px 36px 0 36px; }
  .how h3 { font-size: 30px; font-weight: 700; }
  .how p { font-size: 15.5px; line-height: 1.25; margin-top: 14px; color: #eeeeee; }
  .contact { left: 635px; width: 171px; padding: 12px 28px 0 12px; text-align: right; }
  .contact h3 { font-size: 23px; font-weight: 700; text-align: left; padding-left: 16px; margin-bottom: 18px; }
  .contact dt { font-size: 15.5px; font-weight: 700; color: var(--orange); line-height: 1.3; }
  .contact dd { font-size: 15.5px; color: #eeeeee; line-height: 1.3; }
  .costs {
    position: absolute; left: 0; top: 1027px; width: 806px; height: 96px;
    background: var(--orange); color: var(--white);
    padding: 10px 32px 0 32px;
  }
  .costs h3 { font-size: 28px; font-weight: 700; line-height: 1.1; }
  .costs p { font-size: 13.5px; line-height: 1.3; margin-top: 6px; }
  .costs strong { font-weight: 700; }
  .footer-band {
    position: absolute; left: 0; top: 1123px; width: 806px; height: 9px;
    background: #9a9a9a;
  }
</style>
</head>
<body>
  <main class="flyer">
    <div class="hero" role="img" aria-label="Photo of two business professionals reviewing a tablet in a bright office, colleagues blurred behind"></div>
    <div class="hero-title">
      <h1>PLUM Program</h1>
      <p>Get Plum Now !</p>
    </div>
    <div class="hero-band"></div>

    <section class="intro">
      <h2>Payment Loss &amp; <span class="accent">Underpayment Management</span></h2>
      <p>At Talvo Financial, PLUM locates underpaid claims and turns write offs into added revenue. PLUM uses a genius revenue cycle application that identifies potentially underpaid claims for hospitals. Once revenue has been located, our medical billers correct the claims and appeal to insurance for payment.</p>
    </section>
    <div class="divider"></div>

    <section class="panel how">
      <h3>How <span class="accent">PLUM</span> works ?</h3>
      <p>Remote Evaluation: With a secure and temporary login into any healthcare operating system a random account evaluation is conducted by a highly skilled revenue cycle auditor.<br>
      Data Exchange: When missed revenue is found, a simple data exchange will be recommended. Through the exchange, PLUM will arrange to connect your claims data into the PLUM work flow.<br>
      Collections: PLUM disperses underpaid claims to our medical billers for prompt recovery.</p>
    </section>

    <aside class="panel contact">
      <h3>Contact <span class="accent">Us</span></h3>
      <dl>
        <dt>Phone</dt><dd>000-000-000</dd>
        <dt>Fax</dt><dd>000-000-000</dd>
        <dt>Email</dt><dd>Youremailhere</dd>
        <dt>Address</dt><dd>Your Address here</dd>
      </dl>
    </aside>

    <section class="costs">
      <h3>Costs</h3>
      <p>PLUM charges nothing unless it finds and collects lost revenue for you!<br><strong>GET PLUM TODAY!</strong></p>
    </section>
    <div class="footer-band"></div>
  </main>
</body>
</html>
```